VOIP Telephony Flyer

I am looking for different design styles using my default flyer template and getting designers input and design views. <br/>You MUST use my default style template and make modifications but I would like the color scheme to remain the same. <br/>You MUST use the world grayed out back ground.<br/>You can modify the RED/BLACK color orientations based on your design.<br/>You must incorporate the telephone image as part of the illustration and leave room for 10 bullet points just as Features, PRICING, and contact information.<br/>Corner logo can be changed from location.<br/>design must meet 300dpi resolution for printing quality
Look and feel
Each slider illustrates characteristics of the customer's brand and the style your logo design should communicate.

```html
<!DOCTYPE html>
<html lang="en">
<head>
<meta charset="utf-8">
<title>Signalwide Networks – VoIP Telephony Flyer</title>
<link href="https://fonts.googleapis.com/css2?family=Jura:wght@400;500&family=Montserrat:wght@500;700;800&display=swap" rel="stylesheet">
<style>
  :root {
    --navy: #0e1f2a;
    --navy-deep: #08161f;
    --red: #dc1f26;
    --map-grey: #4a585f;
    --photo-dark: #3a3a3a;
    --photo-light: #8a8783;
    --white: #ffffff;
  }
  html, body {
    margin: 0;
    padding: 0;
    width: 959px;
    height: 1200px;
    overflow: hidden;
    background: var(--navy);
  }
  .flyer {
    position: relative;
    width: 959px;
    height: 1200px;
    overflow: hidden;
    background: linear-gradient(160deg, var(--navy) 0%, var(--navy-deep) 100%);
    font-family: "Montserrat", sans-serif;
    color: var(--white);
  }
  .flyer-shapes {
    position: absolute;
    inset: 0;
  }
  .brand-name {
    position: absolute;
    left: 139px;
    top: 98px;
    transform: translate(-50%, -50%);
    font-family: "Jura", sans-serif;
    font-weight: 500;
    font-size: 18px;
    color: var(--navy);
    letter-spacing: 0.5px;
  }
  .headline {
    position: absolute;
    left: 20px;
    width: 400px;
    top: 262px;
    margin: 0;
    text-align: center;
    font-family: "Jura", sans-serif;
    font-weight: 500;
    font-size: 50px;
    line-height: 48px;
    letter-spacing: 0;
    text-transform: uppercase;
  }
  .contact {
    position: absolute;
    right: 27px;
    top: 1070px;
    text-align: right;
  }
  .contact-phone {
    margin: 0;
    font-weight: 700;
    font-size: 54px;
    line-height: 58px;
    letter-spacing: 1px;
  }
  .contact-web {
    margin: 2px 0 0;
    font-weight: 700;
    font-size: 20px;
    line-height: 26px;
  }
  .contact-address {
    margin: 8px 4px 0 0;
    font-weight: 500;
    font-size: 13px;
    line-height: 16px;
  }
</style>
</head>
<body>
<main class="flyer">
  <svg class="flyer-shapes" width="959" height="1200" viewBox="0 0 959 1200">
    <defs>
      <linearGradient id="photo-top" x1="0" y1="0" x2="1" y2="1">
        <stop offset="0" stop-color="var(--photo-light)"/>
        <stop offset="1" stop-color="var(--photo-dark)"/>
      </linearGradient>
      <linearGradient id="photo-bottom" x1="0" y1="0" x2="1" y2="1">
        <stop offset="0" stop-color="var(--photo-light)"/>
        <stop offset="1" stop-color="#2a2a2a"/>
      </linearGradient>
      <radialGradient id="map-tone" cx="0.5" cy="0.5" r="0.5">
        <stop offset="0" stop-color="var(--map-grey)" stop-opacity="0.95"/>
        <stop offset="0.6" stop-color="var(--map-grey)" stop-opacity="0.75"/>
        <stop offset="1" stop-color="var(--map-grey)" stop-opacity="0"/>
      </radialGradient>
    </defs>

    <ellipse class="world-map" cx="690" cy="600" rx="340" ry="380" fill="url(#map-tone)" role="img" aria-label="Greyed-out world map background"/>

    <polygon class="photo-desk-phone-top" points="437,0 959,0 959,407" fill="url(#photo-top)" role="img" aria-label="Photo of a touchscreen desk phone on an office desk"/>
    <polygon class="photo-desk-phone-bottom" points="0,589 728,1200 0,1200" fill="url(#photo-bottom)" role="img" aria-label="Close-up photo of a touchscreen IP desk phone showing a contact list"/>

    <polygon class="band-red-top" points="0,0 437,0 582,112 0,262" fill="var(--red)"/>
    <polygon class="band-red-bottom" points="290,1200 582,1052 770,1200" fill="var(--red)"/>

    <circle class="brand-badge" cx="139" cy="98" r="82" fill="var(--white)"/>
  </svg>

  <div class="brand-name">Signalwide</div>

  <h1 class="headline">Signalwide<br>Networks</h1>

  <section class="contact">
    <p class="contact-phone">305-555-0148</p>
    <p class="contact-web">www.SignalwideNetworks.com</p>
    <p class="contact-address">2480 Harbor Lane - Suite 210 - Coral Bay Florida 33100</p>
  </section>
</main>
</body>
</html>
```